Business card for exciting VC company

Should look simple, crisp, and modern.

Industry/Entity Type

Venture Capital

Contact Information for Business Card

Would like to see at least one design that has our blue on the back with the tagline "Renewing Foundational Markets" and white front with contact details.

Font styles to use
Sans Serif

Requirements
Must have
• Logo

Gregory Tallis
gtallis@brindlewave.vc
Managing Partner
M (628)354-xxxx

```html
<!DOCTYPE html>
<html lang="en">
<head>
<meta charset="utf-8">
<title>Brindlewave Capital – Business Card</title>
<link href="https://fonts.googleapis.com/css2?family=Lato:wght@400;700&display=swap" rel="stylesheet">
<style>
  :root {
    --brand-blue: #4283c4;
    --line-blue: #1f74c2;
    --ink: #141414;
    --paper: #ffffff;
    --stage: #2a2a2a;
  }
  * { margin: 0; padding: 0; box-sizing: border-box; }
  html, body { width: 1200px; height: 900px; overflow: hidden; }
  body {
    background: var(--stage);
    font-family: 'Lato', sans-serif;
    position: relative;
  }
  .card {
    position: absolute;
    left: 320px;
    width: 560px;
    height: 320px;
    overflow: hidden;
  }
  .card-back { top: 110px; background: var(--brand-blue); }
  .card-front { top: 470px; background: var(--paper); }

  .corner-bar {
    position: absolute;
    bottom: 0;
    width: 32px;
    height: 6px;
  }
  .corner-bar.left { left: 0; }
  .corner-bar.right { right: 0; }
  .card-back .corner-bar { background: var(--paper); }
  .card-front .corner-bar { background: var(--brand-blue); }

  .wordmark {
    font-family: 'Lato', sans-serif;
    font-weight: 700;
    color: var(--ink);
    letter-spacing: 0.12em;
    text-transform: uppercase;
    display: flex;
    align-items: center;
    gap: 12px;
    white-space: nowrap;
  }
  .wordmark-square {
    width: 14px;
    height: 14px;
    background: var(--ink);
    flex: none;
  }
  .card-back .wordmark {
    position: absolute;
    top: 120px;
    left: 0;
    right: 0;
    justify-content: center;
    font-size: 30px;
  }
  .tagline {
    position: absolute;
    bottom: 22px;
    left: 0;
    right: 0;
    text-align: center;
    color: var(--paper);
    font-weight: 700;
    font-size: 13px;
    letter-spacing: 0.06em;
    text-transform: uppercase;
  }

  .card-front .wordmark {
    position: absolute;
    top: 36px;
    left: 36px;
    font-size: 22px;
  }
  .contact-name {
    position: absolute;
    top: 122px;
    left: 52px;
    color: var(--brand-blue);
    font-weight: 700;
    font-size: 15px;
    letter-spacing: 0.03em;
    text-transform: uppercase;
  }
  .contact-role {
    position: absolute;
    top: 143px;
    left: 52px;
    color: var(--ink);
    font-size: 14px;
  }
  .divider {
    position: absolute;
    top: 176px;
    left: 52px;
    right: 40px;
    height: 1.5px;
    background: var(--line-blue);
  }
  .contact-list {
    position: absolute;
    top: 196px;
    left: 52px;
    list-style: none;
    color: var(--ink);
    font-size: 15px;
  }
  .contact-list li {
    display: flex;
    align-items: center;
    gap: 8px;
    height: 24px;
  }
  .contact-list svg { width: 16px; height: 16px; flex: none; }
</style>
</head>
<body>

  <section class="card card-back" aria-label="Card back">
    <div class="wordmark"><span class="wordmark-square"></span>Brindlewave Capital</div>
    <p class="tagline">Renewing Foundational Markets</p>
    <span class="corner-bar left"></span>
    <span class="corner-bar right"></span>
  </section>

  <section class="card card-front" aria-label="Card front">
    <div class="wordmark"><span class="wordmark-square"></span>Brindlewave Capital</div>
    <h1 class="contact-name">Gregory Tallis</h1>
    <p class="contact-role">Managing Partner</p>
    <div class="divider"></div>
    <ul class="contact-list">
      <li>
        <svg viewBox="0 0 16 16" fill="none" stroke="#4283c4" stroke-width="1.2" aria-hidden="true">
          <circle cx="8" cy="8" r="6.5"/>
          <path d="M5.6 4.8c.4-.3.9-.2 1.1.2l.5 1c.1.3 0 .6-.2.8l-.4.3c.4.9 1 1.5 1.9 1.9l.3-.4c.2-.2.5-.3.8-.2l1 .5c.4.2.5.7.2 1.1-.5.7-1.300.9-2 .6-1.7-.7-3-2-3.700-3.700-.3-.8-.1-1.600.5-2.100z"/>
        </svg>
        (628)354-xxxx
      </li>
      <li>
        <svg viewBox="0 0 16 16" fill="none" stroke="#4283c4" stroke-width="1.2" aria-hidden="true">
          <rect x="1.5" y="3.5" width="13" height="9"/>
          <path d="M1.5 3.5 8 9l6.5-5.5M1.5 12.5 6 8M14.5 12.5 10 8"/>
        </svg>
        gtallis@brindlewave.vc
      </li>
    </ul>
    <span class="corner-bar left"></span>
    <span class="corner-bar right"></span>
  </section>

</body>
</html>
```